Greyfield Ridge Medical Website to make connecting and communicating easier

To create a unique, user-friendly, professional website for patients and professionals to access education/ information, forms, appointments, contact details, and data about us, and for us to have the capacity to link to various cloud-based platforms.
To use the logo design and colour scheme we have just sourced.

WEBSITE to be eye catching, Inspiring and alluring
- efficient and logical
- professional and trustworthy appearance
- health focus "living health matters"
- user friendly
- ability to link with cloud-based software and video conferencing tools/ telehealth
- colours- black/ white teal and ?silver

PAGES:
page 1 - Our clinic and staff, services offered, contact us- address/ map / contact details- social media connections
page 2- patients and visitors - New patient forms to complete, news and patient informtion (educatinal)
page 3 - health professionals -referral forms, research and education
page 3- online appointments
page 4 - Quick links - partners, other services
page 5- privacy policy, disclaimer

HI, Could we please extend the deadline another 5 days, so sorry just struggling with my workload to be able to keep up and I am wanting to liaise more with the designer that I will choose. I am so happy with PixelHarbor and all the designers - thank you! Thank you so much!!

Target Market(s)

Patients - mostly over 60's so the website must be minimal clicks and simple to navigate
Professionals - for education and access forms

Industry/Entity Type

Health Care

Coding

Coded - Design and coding required

Number of Pages Required

5+ page

Font styles to use
Sans Serif
Script

Colors
33b8a4
86cfc6

Requirements
Must have
• WEBSITE to be eye catching, Inspiring and alluring
- efficient and logical
- user friendly

WEBSITE - professional and user friendly
- ability to link with cloud based software and videoconferencing/ telehealth
Nice to have
• clean and crisp presentation
happy for an innovative look
room to add more services and ability to link pages and resources
Should not have
• Please ensure the website is not:
clunky
difficult to navigate
common and cheap looking

```html
<!DOCTYPE html>
<html lang="en">
<head>
<meta charset="utf-8">
<title>Greyfield Ridge Medical – Home Page Layouts</title>
<link rel="stylesheet" href="https://fonts.googleapis.com/css2?family=Raleway:wght@500;600;700&family=Roboto:wght@400;500;700&display=swap">
<style>
:root{
  --teal:#2fab93;
  --teal-light:#86cfc6;
  --ink:#222222;
  --text:#6a6a6a;
  --muted:#9a9a9a;
  --grey-bg:#f1f1f1;
  --footer:#1e1e1e;
  --stage:#cbcbcb;
  --white:#ffffff;
}
*{box-sizing:border-box;margin:0;padding:0}
html,body{width:779px;height:1200px;overflow:hidden}
body{background:var(--stage);font-family:'Roboto',Arial,sans-serif;color:var(--ink);position:relative}
a{color:inherit;text-decoration:none}

.page{position:absolute;width:668px;background:var(--white);transform:scale(.504);transform-origin:0 0;overflow:hidden}
.page--classic{left:39px;top:58px;height:2150px}
.page--cloud{left:403px;top:58px;height:2068px}

/* header */
.site-header{position:absolute;left:0;top:0;width:668px;height:60px;border-top:4px solid var(--teal);background:var(--white);z-index:5}
.brand{position:absolute;left:50px;top:-4px;width:118px;height:86px;background:var(--white);
  clip-path:polygon(0 0,100% 0,100% 82%,88% 100%,12% 100%,0 82%);display:flex;align-items:center;gap:6px;padding:0 10px 8px}
.brand-dot{width:14px;height:14px;border-radius:50%;background:var(--teal);flex:none}
.brand-name{font-family:'Raleway',sans-serif;font-weight:700;font-size:11px;line-height:13px;color:var(--teal)}
.main-nav{position:absolute;left:184px;top:20px;display:flex;align-items:center;gap:11px;font-size:8.2px;font-weight:500;color:var(--ink)}
.main-nav .active{color:var(--teal);border-bottom:2px solid var(--teal);padding-bottom:3px}
.caret{font-size:6px;margin-left:2px}
.btn-pill{display:inline-block;background:var(--teal);color:var(--white);border-radius:12px;font-weight:500;font-size:8px;padding:6px 11px}
.main-nav .btn-pill{margin-left:5px}

/* hero */
.hero{position:absolute;left:0;top:60px;width:668px}
.page--classic .hero{height:375px}
.page--cloud .hero{height:385px}
.hero-photo{position:absolute;inset:0}
.page--classic .hero-photo{background:linear-gradient(100deg,#e4f1fa 0%,#c9e2f3 35%,#a9cfea 60%,#d7e9f5 100%)}
.page--cloud .hero-photo{background:linear-gradient(90deg,#ebe7e3 0%,#d9d2cc 42%,#5d97d2 70%,#3f80c4 100%)}
.hero-shape{position:absolute;left:0;bottom:0;width:668px}
.hero-copy{position:absolute;left:60px;top:106px}
.hero-title{font-family:'Raleway',sans-serif;font-weight:600;font-size:25px;line-height:30px;color:var(--ink)}
.hero-title span{display:block;color:var(--teal)}
.hero-text{margin-top:12px;font-size:9px;line-height:15px;color:var(--ink);width:230px}
.hero-copy .btn-pill{margin-top:17px;font-size:8.5px;font-weight:700;padding:8px 16px}
.slider-dots{position:absolute;left:322px;bottom:30px;display:flex;gap:3px}
.slider-dots i{width:6px;height:6px;border-radius:50%;border:1px solid var(--white)}
.slider-dots i.on{background:var(--white)}
.slider-arrow{position:absolute;top:161px;width:22px;height:22px;border-radius:50%;border:1px solid var(--white);color:var(--white);font-size:12px;line-height:19px;text-align:center}
.slider-arrow--prev{left:18px}
.slider-arrow--next{right:18px}

/* arrow icon in buttons */
.go{display:inline-block;width:8px;height:8px;border-radius:50%;background:currentColor;vertical-align:-1px;margin-left:3px;position:relative}
.go::after{content:"";position:absolute;left:2px;top:2.2px;border-left:3.5px solid var(--teal);border-top:1.8px solid transparent;border-bottom:1.8px solid transparent}
.btn-pill .go::after{border-left-color:var(--teal)}

/* clinic */
.clinic{position:absolute;left:0;top:475px;width:668px;height:250px}
.clinic-frame{position:absolute;left:63px;top:5px;width:240px;height:240px;border-radius:50%;border:3px solid var(--teal);border-right-color:transparent;border-top-color:transparent;transform:rotate(-20deg)}
.clinic-photo{position:absolute;left:72px;top:14px;width:222px;height:222px;border-radius:50%;
  background:linear-gradient(160deg,#5a5350 0%,#3f3a38 40%,#8a6a4c 75%,#a27c55 100%)}
.clinic-copy{position:absolute;left:334px;top:36px;width:276px}
.clinic-copy h2{font-family:'Raleway',sans-serif;font-weight:600;font-size:22px;color:var(--ink)}
.clinic-copy p{margin-top:10px;font-size:8.1px;line-height:15.3px;color:var(--text)}
.clinic-copy .btn-pill{margin-top:14px;font-size:8px;font-weight:700;padding:7px 15px}

/* section title */
.section-title{position:absolute;left:0;width:668px;text-align:center;font-family:'Raleway',sans-serif;font-weight:600;font-size:21px;color:var(--ink)}
.section-title::after{content:"";display:block;width:34px;height:2px;background:var(--teal);margin:5px auto 0}
.section-title--light{color:var(--white)}
.section-title--light::after{background:var(--white)}

/* staff – card style */
.staff-band{position:absolute;left:0;top:725px;width:668px;height:380px}
.staff-band svg{position:absolute;left:0;top:0}
.staff-band .section-title{top:77px}
.staff-card{position:absolute;top:158px;width:175px;height:165px;background:var(--white);box-shadow:0 2px 6px rgba(0,0,0,.08);text-align:center;padding-top:42px}
.staff-avatar{position:absolute;left:57px;top:-30px;width:60px;height:60px;border-radius:50%;background:linear-gradient(180deg,#d8d8d8,#8b8b8b)}
.staff-card h3{font-size:9px;font-weight:700;color:var(--ink)}
.staff-role{font-size:7px;color:var(--muted);margin-top:2px}
.staff-card p{font-size:7.5px;line-height:13.4px;color:var(--text);margin:8px 16px 0}
.staff-card .btn-pill{margin-top:9px;font-size:7px;font-weight:700;padding:5px 15px}

/* staff – portrait grid */
.staff-grid{position:absolute;left:0;top:1165px;width:668px;height:220px}
.staff-grid .section-title{top:10px}
.staff-tile{position:absolute;top:61px;width:128px;height:155px;border:1px solid #ddd;background:var(--white);text-align:center}
.staff-portrait{margin:3px;height:110px;background:linear-gradient(180deg,#e6e6e6,#c4c4c4)}
.staff-tile h3{margin-top:7px;font-size:8px;font-weight:500;color:var(--ink)}
.staff-tile span{display:block;font-size:6.5px;color:var(--muted);margin-top:3px}

/* services */
.services{position:absolute;left:0;width:668px;background:linear-gradient(180deg,#31ad95,#2ea48d)}
.page--classic .services{top:1103px;height:377px}
.page--cloud .services{top:786px;height:337px}
.services .section-title{top:30px}
.service-card{position:absolute;width:263px;height:101px;background:var(--white);padding:16px 16px 0 55px}
.service-card svg{position:absolute;left:12px;top:15px}
.service-card h3{font-size:8.4px;font-weight:500;color:var(--ink)}
.service-card p{margin-top:7px;font-size:7.3px;line-height:12.3px;color:var(--text)}
.service-card a{display:inline-block;margin-top:6px;font-size:7.3px;font-weight:700;color:var(--teal)}
.service-card a .go{width:7px;height:7px}
.service-card a .go::after{border-left-color:var(--white);left:2px;top:1.7px;border-left-width:3px}
.clouds{position:absolute;left:0;bottom:0;width:668px}

/* contact */
.contact{position:absolute;left:0;width:668px;height:310px}
.page--classic .contact{top:1520px}
.page--cloud .contact{top:1442px}
.contact .section-title{top:0}
.contact-heading{position:absolute;left:62px;top:72px;font-family:'Raleway',sans-serif;font-weight:600;font-size:18px;color:var(--teal)}
.contact-list{position:absolute;left:58px;top:108px;width:220px;list-style:none}
.contact-list li{position:relative;padding-left:37px;height:40px;font-size:7.8px;line-height:13px;color:var(--ink)}
.contact-list li svg{position:absolute;left:0;top:0}
.contact-list b{display:block;font-weight:700}
.social{display:flex;gap:5px}
.social i{width:17px;height:17px;border-radius:50%;background:var(--teal)}
.contact .social{position:absolute;left:62px;top:280px}
.contact-map{position:absolute;left:304px;top:73px;width:275px;height:237px;border:3px solid var(--white);box-shadow:0 0 4px rgba(0,0,0,.15);
  background:linear-gradient(135deg,#cfe7cf 0%,#f0ead6 30%,#efe8d4 60%,#bfe0c6 100%)}

/* footer */
.site-footer{position:absolute;left:0;bottom:0;width:668px;background:var(--footer);color:var(--white)}
.page--classic .site-footer{height:250px}
.page--cloud .site-footer{height:253px}
.footer-shape{position:absolute;left:0;top:0;width:668px}
.footer-cols{position:absolute;left:62px;display:flex}
.page--classic .footer-cols{top:96px}
.page--cloud .footer-cols{top:93px}
.footer-col h4{font-size:9px;font-weight:500;text-transform:uppercase;margin-bottom:9px}
.footer-col ul{list-style:none;font-size:7.5px;line-height:18px}
.footer-col--links li::before{content:"»";margin-right:5px}
.col-quick{width:111px}
.col-important{width:118px}
.col-contact{width:166px}
.footer-contact li{position:relative;padding-left:14px;line-height:12px;margin-bottom:6px}
.footer-contact svg{position:absolute;left:0;top:2px}
.subscribe{display:flex;width:148px;height:19px;background:var(--white);border-radius:10px;overflow:hidden;margin-bottom:8px}
.subscribe span{flex:1;font-size:7px;color:var(--muted);padding:5px 0 0 9px}
.subscribe b{background:var(--teal);border-radius:10px;font-size:7.5px;font-weight:700;padding:5px 9px;color:var(--white)}
.site-footer .social i{background:transparent;border:1.5px solid var(--white);width:18px;height:18px}
.footer-rule{position:absolute;left:62px;right:62px;height:1px;background:#3a3a3a}
.page--classic .footer-rule{top:210px}
.copyright{position:absolute;left:0;width:668px;text-align:center;font-size:7.8px}
.page--classic .copyright{top:226px}
.page--cloud .copyright{top:230px}
</style>
</head>
<body>

<svg width="0" height="0" style="position:absolute" aria-hidden="true">
  <defs>
    <symbol id="i-pin" viewBox="0 0 24 24"><path d="M12 2a7 7 0 0 0-7 7c0 5 7 13 7 13s7-8 7-13a7 7 0 0 0-7-7z" fill="currentColor"/><circle cx="12" cy="9" r="2.6" fill="#fff"/></symbol>
    <symbol id="i-phone" viewBox="0 0 24 24"><path d="M6 3l3 1 1 4-2 2c1 3 3 5 6 6l2-2 4 1 1 3-3 3C10 21 3 14 3 6z" fill="none" stroke="currentColor" stroke-width="1.6"/></symbol>
    <symbol id="i-mail" viewBox="0 0 24 24"><rect x="2.5" y="5" width="19" height="14" fill="none" stroke="currentColor" stroke-width="1.6"/><path d="M2.5 5l9.5 8 9.5-8" fill="none" stroke="currentColor" stroke-width="1.6"/></symbol>
    <symbol id="i-fax" viewBox="0 0 24 24"><rect x="3" y="9" width="5" height="12" fill="none" stroke="currentColor" stroke-width="1.5"/><rect x="8" y="7" width="13" height="14" fill="none" stroke="currentColor" stroke-width="1.5"/><path d="M11 3h7v4h-7zM11 11h7M11 14h2M15 14h2M11 17h2M15 17h2" fill="none" stroke="currentColor" stroke-width="1.3"/></symbol>
    <symbol id="i-cloud" viewBox="0 0 32 32"><path d="M9 20a5 5 0 0 1 0-10 7 7 0 0 1 13-1 5 5 0 0 1 2 11z" fill="none" stroke="currentColor" stroke-width="1.4"/><path d="M16 14v14M12 18l4 3 4-3" fill="none" stroke="currentColor" stroke-width="1.4"/></symbol>
    <symbol id="i-monitor" viewBox="0 0 32 32"><rect x="3" y="6" width="26" height="17" fill="none" stroke="currentColor" stroke-width="1.4"/><path d="M7 19v-4M10 19v-7M13 19v-5M16 19v-8M19 19v-3M22 19v-6M25 19v-4M12 27h8M16 23v4" fill="none" stroke="currentColor" stroke-width="1.3"/></symbol>
    <symbol id="i-network" viewBox="0 0 32 32"><rect x="3" y="4" width="8" height="7" fill="none" stroke="currentColor" stroke-width="1.3"/><rect x="21" y="12" width="8" height="7" fill="none" stroke="currentColor" stroke-width="1.3"/><rect x="3" y="21" width="8" height="7" fill="none" stroke="currentColor" stroke-width="1.3"/><path d="M11 7h5v18h-5M16 15h5" fill="none" stroke="currentColor" stroke-width="1.3"/></symbol>
    <symbol id="i-screen-plus" viewBox="0 0 32 32"><rect x="3" y="8" width="26" height="18" fill="none" stroke="currentColor" stroke-width="1.4"/><path d="M16 2v8M13 5l3-3 3 3M20 17h6M23 14v6" fill="none" stroke="currentColor" stroke-width="1.4"/><circle cx="11" cy="15" r="2.5" fill="none" stroke="currentColor" stroke-width="1.3"/><path d="M6 23c1-4 9-4 10 0" fill="none" stroke="currentColor" stroke-width="1.3"/></symbol>
  </defs>
</svg>

<!-- ============ Layout A: classic wave ============ -->
<main class="page page--classic">
  <header class="site-header">
    <div class="brand"><span class="brand-dot"></span><span class="brand-name">Greyfield Ridge<br>Medical</span></div>
    <nav class="main-nav">
      <a class="active">Home</a>
      <a>Our Clinic<span class="caret">▼</span></a>
      <a>Patients &amp; Visitors<span class="caret">▼</span></a>
      <a>Health Professionals<span class="caret">▼</span></a>
      <a>Contact</a>
      <a class="btn-pill">Online Appointments</a>
    </nav>
  </header>

  <section class="hero">
    <div class="hero-photo" role="img" aria-label="Doctor in a white coat holding a tablet with floating medical data graphics"></div>
    <svg class="hero-shape" width="668" height="110" viewBox="0 0 668 110" aria-hidden="true">
      <path d="M0 12C180 80 430 100 668 0V110H0Z" fill="var(--teal)"/>
      <path d="M0 38C200 120 450 118 668 28V110H0Z" fill="#fff"/>
    </svg>
    <div class="hero-copy">
      <h1 class="hero-title">LIVING HEALTHY<span>MATTERS</span></h1>
      <p class="hero-text">Lorem ipsum dolor sit amet, consectetur adipiscing elit, sed do eiusmod tempor incididunt</p>
      <a class="btn-pill">GET STARTED <i class="go" style="color:#fff"></i></a>
    </div>
    <div class="slider-dots"><i></i><i class="on"></i><i></i></div>
  </section>

  <section class="clinic">
    <div class="clinic-frame" aria-hidden="true"></div>
    <div class="clinic-photo" role="img" aria-label="Clinic reception desk in a modern waiting area"></div>
    <div class="clinic-copy">
      <h2>OUR CLINIC</h2>
      <p>Sed ut perspiciatis unde omnis iste natus sit voluptatem accusantium doloremque laudantium, totam rem aperiam, eaque ipsa quae ab illo inventore veritatis et quasi architecto beatae vitae dicta sunt explicabo. Nemo enim ipsam voluptatem quia voluptas sit aspernatur aut odit aut fugit, sed quia consequuntur magni dolores</p>
      <p>Lorem ipsum dolor sit amet, consectetur adipiscing elit, sed do eiusmod tempor et dolore magna aliqua.</p>
      <a class="btn-pill">READ MORE <i class="go" style="color:#fff"></i></a>
    </div>
  </section>

  <section class="staff-band">
    <svg width="668" height="380" viewBox="0 0 668 380" aria-hidden="true">
      <path d="M0 15C150 70 300 60 420 40S620 20 668 38V380H0Z" fill="var(--grey-bg)"/>
      <path d="M0 15C90 48 170 62 240 62" fill="none" stroke="var(--teal)" stroke-width="2"/>
    </svg>
    <h2 class="section-title">OUR STAFF</h2>
    <article class="staff-card" style="left:55px">
      <div class="staff-avatar" role="img" aria-label="Staff portrait"></div>
      <h3>JOHN DOE</h3><div class="staff-role">Lorem ipsum dolor</div>
      <p>Sed ut perspiciatis unde omnis iste natus error sit voluptatem accusantium doloremque laudantium, totam rem aperiam, eaque ipsa quae</p>
      <a class="btn-pill">VIEW BIO</a>
    </article>
    <article class="staff-card" style="left:243px">
      <div class="staff-avatar" role="img" aria-label="Staff portrait"></div>
      <h3>JOHN DOE</h3><div class="staff-role">Lorem ipsum dolor</div>
      <p>Sed ut perspiciatis unde omnis iste natus error sit voluptatem accusantium doloremque laudantium, totam rem aperiam, eaque ipsa quae</p>
      <a class="btn-pill">VIEW BIO</a>
    </article>
    <article class="staff-card" style="left:431px">
      <div class="staff-avatar" role="img" aria-label="Staff portrait"></div>
      <h3>JOHN DOE</h3><div class="staff-role">Lorem ipsum dolor</div>
      <p>Sed ut perspiciatis unde omnis iste natus error sit voluptatem accusantium doloremque laudantium, totam rem aperiam, eaque ipsa quae</p>
      <a class="btn-pill">VIEW BIO</a>
    </article>
  </section>

  <section class="services">
    <h2 class="section-title section-title--light">OUR SERVICES</h2>
    <article class="service-card" style="left:64px;top:85px"><svg width="32" height="32" style="color:var(--teal)"><use href="#i-cloud"/></svg><h3>Lorem ipsum dolor sit consectetur</h3><p>Sed ut perspiciatis unde omnis iste natus error sit voluptatem accusantium doloremque laudantium, totam rem aperiam, eaque</p><a>READ MORE <i class="go"></i></a></article>
    <article class="service-card" style="left:341px;top:85px"><svg width="32" height="32" style="color:var(--teal)"><use href="#i-monitor"/></svg><h3>Lorem ipsum dolor sit consectetur</h3><p>Sed ut perspiciatis unde omnis iste natus error sit voluptatem accusantium doloremque laudantium, totam rem aperiam, eaque</p><a>READ MORE <i class="go"></i></a></article>
    <article class="service-card" style="left:64px;top:199px"><svg width="32" height="32" style="color:var(--teal)"><use href="#i-network"/></svg><h3>Lorem ipsum dolor sit consectetur</h3><p>Sed ut perspiciatis unde omnis iste natus error sit voluptatem accusantium doloremque laudantium, totam rem aperiam, eaque</p><a>READ MORE <i class="go"></i></a></article>
    <article class="service-card" style="left:341px;top:199px"><svg width="32" height="32" style="color:var(--teal)"><use href="#i-screen-plus"/></svg><h3>Lorem ipsum dolor sit consectetur</h3><p>Sed ut perspiciatis unde omnis iste natus error sit voluptatem accusantium doloremque laudantium, totam rem aperiam, eaque</p><a>READ MORE <i class="go"></i></a></article>
    <svg class="clouds" width="668" height="34" viewBox="0 0 668 34" aria-hidden="true">
      <path d="M0 34V22Q15 8 32 18Q50 2 75 16Q92 6 110 18Q140 -2 170 16Q190 8 205 20Q230 4 255 18Q290 -4 330 16Q355 6 375 18Q400 0 430 16Q455 6 475 20Q505 2 540 18Q565 8 585 20Q615 4 640 18Q655 10 668 16V34Z" fill="#fff"/>
    </svg>
  </section>

  <section class="contact">
    <h2 class="section-title">CONTACT US</h2>
    <h3 class="contact-heading">contact details</h3>
    <ul class="contact-list">
      <li><svg width="20" height="22" style="color:var(--teal)"><use href="#i-pin"/></svg>123, Lorem ipsum dolor sit amet, consectetur adipiscing elit, sed do</li>
      <li><svg width="22" height="22" style="color:var(--teal)"><use href="#i-phone"/></svg><b>PHONE NUMBER</b>888 888 8888</li>
      <li><svg width="22" height="22" style="color:var(--teal)"><use href="#i-mail"/></svg><b>EMAIL</b>info@Greyfield Ridge Medical.com</li>
      <li><svg width="22" height="22" style="color:var(--teal)"><use href="#i-fax"/></svg><b>FAX</b>123 456 7890</li>
    </ul>
    <div class="social"><i></i><i></i><i></i></div>
    <div class="contact-map" role="img" aria-label="Map showing the clinic location"></div>
  </section>

  <footer class="site-footer">
    <svg class="footer-shape" width="668" height="100" viewBox="0 0 668 100" aria-hidden="true">
      <path d="M0 0H668V6C470 10 220 30 0 70Z" fill="#fff"/>
      <path d="M0 70C220 30 470 10 668 6V78C470 40 230 52 0 92Z" fill="var(--teal)"/>
    </svg>
    <div class="footer-cols">
      <div class="footer-col footer-col--links col-quick"><h4>Quick Links</h4><ul><li>Home</li><li>Partners</li><li>Other services</li><li>News</li><li>Patient information</li></ul></div>
      <div class="footer-col footer-col--links col-important"><h4>Important</h4><ul><li>Terms of Use</li><li>Site Map</li><li>Privacy Policy</li><li>Disclaimer</li></ul></div>
      <div class="footer-col col-contact"><h4>Contact Us</h4><ul class="footer-contact">
        <li><svg width="8" height="8" style="color:#fff"><use href="#i-pin"/></svg>870 Lorem ipsum dolor sit<br>amet, consectetu</li>
        <li><svg width="8" height="8" style="color:#fff"><use href="#i-phone"/></svg>888 888 8888</li>
        <li><svg width="8" height="8" style="color:#fff"><use href="#i-fax"/></svg>+ 123 456 7892</li>
        <li><svg width="8" height="8" style="color:#fff"><use href="#i-mail"/></svg>hail@greyfieldridgemedical.com</li></ul></div>
      <div class="footer-col"><h4>Subscribe Today!</h4><div class="subscribe"><span>Enter your email</span><b>SUBMIT</b></div><div class="social"><i></i><i></i><i></i><i></i></div></div>
    </div>
    <div class="footer-rule"></div>
    <p class="copyright">© 2020 Greyfield Ridge Medical. &nbsp;|&nbsp; All Rights Reserved</p>
  </footer>
</main>

<!-- ============ Layout B: cloud edges ============ -->
<main class="page page--cloud">
  <header class="site-header">
    <div class="brand"><span class="brand-dot"></span><span class="brand-name">Greyfield Ridge<br>Medical</span></div>
    <nav class="main-nav">
      <a class="active">Home</a>
      <a>Our Clinic<span class="caret">▼</span></a>
      <a>Patients &amp; Visitors<span class="caret">▼</span></a>
      <a>Health Professionals<span class="caret">▼</span></a>
      <a>Contact</a>
      <a class="btn-pill">Online Appointments</a>
    </nav>
  </header>

  <section class="hero">
    <div class="hero-photo" role="img" aria-label="Clinician in blue scrubs holding out a hand beneath cloud data security graphics"></div>
    <svg class="hero-shape" width="668" height="70" viewBox="0 0 668 70" aria-hidden="true">
      <path d="M0 70V60Q30 30 70 48Q100 10 150 35Q190 -2 240 30Q290 5 330 28Q380 0 430 30Q470 12 500 34Q540 -4 590 22Q630 8 668 20V70Z" fill="#fff"/>
    </svg>
    <div class="hero-copy">
      <h1 class="hero-title">LIVING HEALTHY<span>MATTERS</span></h1>
      <p class="hero-text">Lorem ipsum dolor sit amet, consectetur adipiscing elit, sed do eiusmod tempor incididunt</p>
      <a class="btn-pill">GET STARTED <i class="go" style="color:#fff"></i></a>
    </div>
    <span class="slider-arrow slider-arrow--prev">‹</span>
    <span class="slider-arrow slider-arrow--next">›</span>
  </section>

  <section class="clinic">
    <div class="clinic-frame" aria-hidden="true"></div>
    <div class="clinic-photo" role="img" aria-label="Clinic reception desk in a modern waiting area"></div>
    <div class="clinic-copy">
      <h2>OUR CLINIC</h2>
      <p>Sed ut perspiciatis unde omnis iste natus sit voluptatem accusantium doloremque laudantium, totam rem aperiam, eaque ipsa quae ab illo inventore veritatis et quasi architecto beatae vitae dicta sunt explicabo. Nemo enim ipsam voluptatem quia voluptas sit aspernatur aut odit aut fugit, sed quia consequuntur magni dolores</p>
      <p>Lorem ipsum dolor sit amet, consectetur adipiscing elit, sed do eiusmod tempor et dolore magna aliqua.</p>
      <a class="btn-pill">READ MORE <i class="go" style="color:#fff"></i></a>
    </div>
  </section>

  <section class="services">
    <h2 class="section-title section-title--light">OUR SERVICES</h2>
    <article class="service-card" style="left:64px;top:79px"><svg width="32" height="32" style="color:var(--teal)"><use href="#i-cloud"/></svg><h3>Lorem ipsum dolor sit consectetur</h3><p>Sed ut perspiciatis unde omnis iste natus error sit voluptatem accusantium doloremque laudantium, totam rem aperiam, eaque</p><a>READ MORE <i class="go"></i></a></article>
    <article class="service-card" style="left:341px;top:79px"><svg width="32" height="32" style="color:var(--teal)"><use href="#i-monitor"/></svg><h3>Lorem ipsum dolor sit consectetur</h3><p>Sed ut perspiciatis unde omnis iste natus error sit voluptatem accusantium doloremque laudantium, totam rem aperiam, eaque</p><a>READ MORE <i class="go"></i></a></article>
    <article class="service-card" style="left:64px;top:193px"><svg width="32" height="32" style="color:var(--teal)"><use href="#i-network"/></svg><h3>Lorem ipsum dolor sit consectetur</h3><p>Sed ut perspiciatis unde omnis iste natus error sit voluptatem accusantium doloremque laudantium, totam rem aperiam, eaque</p><a>READ MORE <i class="go"></i></a></article>
    <article class="service-card" style="left:341px;top:193px"><svg width="32" height="32" style="color:var(--teal)"><use href="#i-screen-plus"/></svg><h3>Lorem ipsum dolor sit consectetur</h3><p>Sed ut perspiciatis unde omnis iste natus error sit voluptatem accusantium doloremque laudantium, totam rem aperiam, eaque</p><a>READ MORE <i class="go"></i></a></article>
  </section>

  <section class="staff-grid">
    <h2 class="section-title">OUR STAFF</h2>
    <article class="staff-tile" style="left:62px"><div class="staff-portrait" role="img" aria-label="Staff portrait"></div><h3>Daniel R. Marsh M.D.</h3><span>Lorem ipsum</span></article>
    <article class="staff-tile" style="left:200px"><div class="staff-portrait" role="img" aria-label="Staff portrait"></div><h3>Daniel R. Marsh M.D.</h3><span>Lorem ipsum</span></article>
    <article class="staff-tile" style="left:339px"><div class="staff-portrait" role="img" aria-label="Staff portrait"></div><h3>Daniel R. Marsh M.D.</h3><span>Lorem ipsum</span></article>
    <article class="staff-tile" style="left:477px"><div class="staff-portrait" role="img" aria-label="Staff portrait"></div><h3>Daniel R. Marsh M.D.</h3><span>Lorem ipsum</span></article>
  </section>

  <section class="contact">
    <h2 class="section-title">CONTACT US</h2>
    <h3 class="contact-heading">contact details</h3>
    <ul class="contact-list">
      <li><svg width="20" height="22" style="color:var(--teal)"><use href="#i-pin"/></svg>123, Lorem ipsum dolor sit amet, consectetur adipiscing elit, sed do</li>
      <li><svg width="22" height="22" style="color:var(--teal)"><use href="#i-phone"/></svg><b>PHONE NUMBER</b>888 888 8888</li>
      <li><svg width="22" height="22" style="color:var(--teal)"><use href="#i-mail"/></svg><b>EMAIL</b>info@Greyfield Ridge Medical.com</li>
      <li><svg width="22" height="22" style="color:var(--teal)"><use href="#i-fax"/></svg><b>FAX</b>123 456 7890</li>
    </ul>
    <div class="social"><i></i><i></i><i></i></div>
    <div class="contact-map" role="img" aria-label="Map showing the clinic location"></div>
  </section>

  <footer class="site-footer">
    <svg class="footer-shape" width="668" height="80" viewBox="0 0 668 80" aria-hidden="true">
      <path d="M0 0H668V18Q640 40 600 28Q560 60 510 40Q470 70 420 48Q370 78 320 52Q280 72 240 50Q200 72 160 46Q120 62 90 36Q50 56 20 32Q8 40 0 36Z" fill="#fff"/>
    </svg>
    <div class="footer-cols">
      <div class="footer-col footer-col--links col-quick"><h4>Quick Links</h4><ul><li>Home</li><li>Partners</li><li>Other services</li><li>News</li><li>Patient information</li></ul></div>
      <div class="footer-col footer-col--links col-important"><h4>Important</h4><ul><li>Terms of Use</li><li>Site Map</li><li>Privacy Policy</li><li>Disclaimer</li></ul></div>
      <div class="footer-col col-contact"><h4>Contact Us</h4><ul class="footer-contact">
        <li><svg width="8" height="8" style="color:#fff"><use href="#i-pin"/></svg>870 Lorem ipsum dolor sit<br>amet, consectetu</li>
        <li><svg width="8" height="8" style="color:#fff"><use href="#i-phone"/></svg>888 888 8888</li>
        <li><svg width="8" height="8" style="color:#fff"><use href="#i-fax"/></svg>+ 123 456 7892</li>
        <li><svg width="8" height="8" style="color:#fff"><use href="#i-mail"/></svg>hail@greyfieldridgemedical.com</li></ul></div>
      <div class="footer-col"><h4>Subscribe Today!</h4><div class="subscribe"><span>Enter your email</span><b>SUBMIT</b></div><div class="social"><i></i><i></i><i></i><i></i></div></div>
    </div>
    <p class="copyright">© 2020 Greyfield Ridge Medical. &nbsp;|&nbsp; All Rights Reserved</p>
  </footer>
</main>

</body>
</html>
```